TovaLamarpe - Israeli Mental Health Website

We are developing an Israeli website for mental health. The website will be both in English and in Hebrew. We have a logo and would like a website design based on the logo and the logos colors (attached).

Attached is a doc that contains the website requirements.

We would like to have an icon for each of the sidebar categories, an image for each of the pages (including each of the sidebar category pages).

Target Market(s)

Adults 18-80

Industry/Entity Type

Mental Health

Number of Pages Required

5+ page

Font styles to use
Sans Serif

Colors

Designer to choose colors to be used in the design.

```html
<!DOCTYPE html>
<html lang="en">
<head>
<meta charset="utf-8">
<title>TovaLamarpe – Home Page Layouts</title>
<link href="https://fonts.googleapis.com/css2?family=Inter:wght@400;500;600;700&family=Rubik:wght@400;500;600;700&display=swap" rel="stylesheet">
<style>
:root{
  --blue:#1e6fb9;
  --blue-dark:#16589a;
  --green:#43a53d;
  --green-soft:#5dbb55;
  --ink:#1f2730;
  --muted:#4a525b;
  --navy:#0f1c2a;
  --paper:#ffffff;
}
*{box-sizing:border-box;margin:0;padding:0}
html,body{width:980px;height:1200px;overflow:hidden;background:var(--paper)}
body{position:relative;font-family:"Inter",sans-serif;color:var(--ink)}
.board-title{position:absolute;top:27px;font-family:"Rubik",sans-serif;font-weight:500;font-size:13px;color:var(--blue);width:260px;text-align:center}
.page{position:absolute;top:53px;background:var(--paper);box-shadow:0 1px 6px rgba(0,0,0,.18);overflow:hidden}
.page--v1{left:15px;width:459px;height:1111px}
.page--v2{left:505px;width:460px;height:715px}

.sidebar{position:absolute;left:0;top:0;width:83px;height:250px;background:var(--paper)}
.brand{position:absolute;top:16px;left:0;width:83px;text-align:center;font-family:"Rubik",sans-serif;font-weight:600;font-size:9px;color:var(--blue)}
.brand-dot{display:block;width:14px;height:14px;border-radius:50%;background:var(--green);margin:0 auto 4px}
.cat-list{position:absolute;top:43px;left:5px;list-style:none}
.cat-list li{display:flex;align-items:center;gap:4px;height:15.7px;font-size:4.6px;font-weight:500;color:var(--ink);line-height:1.15}
.cat-list li svg{flex:none;width:8px;height:8px}

.nav{position:absolute;top:12px;display:flex;align-items:center;gap:6px;font-size:6px;font-weight:500}
.nav a{text-decoration:none}
.nav .donate{padding:4px 12px;border-radius:8px;font-weight:600;font-size:6px}
.nav .lang{display:flex;align-items:center;gap:2px;margin-left:6px}
.flag{width:8px;height:5px;background:linear-gradient(#b22 0 20%,#fff 20% 40%,#b22 40% 60%,#fff 60% 80%,#b22 80%);position:relative}
.flag::before{content:"";position:absolute;left:0;top:0;width:3.5px;height:3px;background:#2a3e8c}

.hero{position:absolute;left:83px;top:0;height:250px}
.page--v1 .hero{width:376px;background:linear-gradient(120deg,#eef0f0,#dfe2e3 55%,#e8eaea)}
.page--v1 .nav a{color:var(--blue)}
.page--v1 .nav .donate{background:var(--green);color:#fff}
.page--v1 .nav .lang{color:var(--ink)}
.hero-photo{position:absolute;inset:0}

.page--v2 .hero{width:377px;background:linear-gradient(125deg,#2b86b4 0%,#3a9d8a 50%,#4eaf4c 100%)}
.page--v2 .nav a,.page--v2 .nav .lang{color:#fff}
.page--v2 .nav .donate{border:1px solid #fff;color:#fff}
.hero-title{position:absolute;top:102px;width:100%;text-align:center;font-family:"Rubik",sans-serif;font-weight:700;font-size:29px;color:#fff;letter-spacing:.2px}
.hero-sub{position:absolute;top:140px;left:40px;right:40px;text-align:center;font-size:6px;font-weight:500;line-height:10px;color:#fff}
.scroll-mouse{position:absolute;left:183px;top:223px;width:10px;height:15px;border:1.2px solid #fff;border-radius:6px}
.scroll-mouse::after{content:"";position:absolute;left:3.2px;top:3px;width:1.2px;height:3px;background:#fff;border-radius:1px}

.welcome-title{position:absolute;font-family:"Rubik",sans-serif;font-weight:600;color:var(--blue)}
.page--v1 .welcome-title{left:102px;top:290px;font-size:17.5px}
.welcome-text{position:absolute;font-size:6px;line-height:11px;color:var(--muted)}
.page--v1 .welcome-text{left:102px;top:316px;width:320px}
.page--v2 .welcome-title{left:0;width:460px;text-align:center;top:280px;font-size:17px;font-weight:400;color:var(--ink)}
.page--v2 .welcome-title b{color:var(--blue);font-weight:600}
.page--v2 .welcome-text{left:122px;top:322px;width:262px;text-align:center;line-height:9.2px;font-size:5.8px}

.feature-media{position:absolute;width:126px;height:98px;border-radius:4px}
.feature-frame{position:absolute;width:126px;height:104px;border-bottom:1px solid var(--green)}
.feature-frame.right{border-right:1px solid var(--green)}
.feature-frame.left{border-left:1px solid var(--green)}
.feature-title{position:absolute;font-family:"Rubik",sans-serif;font-weight:500;font-size:12.5px;color:var(--blue)}
.feature-text{position:absolute;width:178px;font-size:6.2px;line-height:9.3px;color:var(--muted)}
.btn{position:absolute;display:inline-flex;align-items:center;gap:3px;height:16px;padding:0 9px;border-radius:8px;font-size:6px;font-weight:600;color:#fff;background:var(--green);white-space:nowrap}
.btn svg{width:6px;height:6px}

.spot-card{position:absolute;left:84px;top:389px;width:336px;height:116px;background:#fff;box-shadow:0 0 6px rgba(0,0,0,.07)}
.spot-card .media{position:absolute;left:6px;top:5px;width:129px;height:106px;border-radius:5px}
.spot-card h3{position:absolute;left:144px;top:20px;font-size:7.5px;font-weight:500;color:var(--ink)}
.spot-card p{position:absolute;left:145px;top:34px;width:178px;font-size:6px;line-height:9.2px;color:var(--muted)}
.spot-card .btn{left:145px;top:76px;border-radius:1px;background:var(--blue)}
.tile{position:absolute;top:539px;width:77px;height:115px;background:#fff;box-shadow:0 0 5px rgba(0,0,0,.07);text-align:center}
.tile .media{position:absolute;left:3px;top:3px;width:71px;height:51px}
.tile h4{position:absolute;top:56px;width:100%;font-size:7.5px;font-weight:500;color:var(--ink)}
.tile p{position:absolute;top:66px;left:8px;right:8px;font-size:5.4px;line-height:8.2px;color:var(--muted)}
.tile .btn{top:93px;left:50%;transform:translateX(-50%);border-radius:1px;height:15px;padding:0 5px;font-size:5.8px}
.tile .btn.blue{background:var(--blue)}

.footer{position:absolute;left:0;right:0;height:29px;background:var(--navy);font-size:4.8px;color:#cfd6dd;display:flex;align-items:center}
.page--v1 .footer{top:1082px}
.page--v2 .footer{top:687px}
.footer .copy{position:absolute;left:38px}
.footer .copy b{color:var(--green-soft);font-weight:500}
.footer .links{position:absolute;left:201px}
.footer .links span{margin:0 4px;color:#8a96a3}
.footer .stamp{position:absolute;right:38px;color:#2f4256}

.thanks{position:absolute;left:580px;width:312px;text-align:center;font-family:"Rubik",sans-serif;font-weight:600}
.thanks .line1{position:absolute;top:813px;width:100%;font-size:33px;color:var(--ink)}
.thanks .line2{position:absolute;top:843px;width:100%;font-size:70px;font-weight:700;color:var(--green)}
</style>
</head>
<body>

<h1 class="board-title" style="left:115px">Home Page V.01</h1>
<h1 class="board-title" style="left:603px">Home Page V.02</h1>

<section class="page page--v1">
  <aside class="sidebar">
    <div class="brand"><span class="brand-dot"></span>TovaLamarpe</div>
    <ul class="cat-list">
      <li><svg viewBox="0 0 10 10"><circle cx="5" cy="5" r="4" fill="#1e6fb9"/></svg>Emergency Mental Help</li>
      <li><svg viewBox="0 0 10 10"><path d="M5 1v4M3 8a2 2 0 004 0 2 2 0 00-4 0" stroke="#1e6fb9" fill="none" stroke-width=".9"/></svg>Suicide</li>
      <li><svg viewBox="0 0 10 10"><circle cx="5" cy="5" r="2.4" stroke="#1e6fb9" fill="none" stroke-width=".9"/><path d="M5 0v2M5 8v2M0 5h2M8 5h2" stroke="#1e6fb9" stroke-width=".9"/></svg>Sexual Assault/<br>Violence Victims</li>
      <li><svg viewBox="0 0 10 10"><circle cx="5" cy="5" r="4" stroke="#1e6fb9" fill="none" stroke-width=".9"/><circle cx="5" cy="5" r="2" stroke="#1e6fb9" fill="none" stroke-width=".7"/></svg>Sexual Assault/<br>Violence Assaulters</li>
      <li><svg viewBox="0 0 10 10"><circle cx="5" cy="3" r="2" stroke="#1e6fb9" fill="none" stroke-width=".9"/><path d="M1 9.5c0-3 8-3 8 0" stroke="#1e6fb9" fill="none" stroke-width=".9"/></svg>Post Trauma</li>
      <li><svg viewBox="0 0 10 10"><circle cx="5" cy="5" r="3.6" stroke="#1e6fb9" fill="none" stroke-width=".9"/><path d="M3.4 6.8c1-1 2.2-1 3.2 0" stroke="#1e6fb9" fill="none" stroke-width=".8"/></svg>Depression</li>
      <li><svg viewBox="0 0 10 10"><path d="M2 9V5a3 3 0 016 0v4" stroke="#1e6fb9" fill="none" stroke-width="1"/></svg>Anxiety</li>
      <li><svg viewBox="0 0 10 10"><circle cx="4.5" cy="4" r="3" stroke="#1e6fb9" fill="none" stroke-width=".9"/><path d="M1 9.5h8" stroke="#1e6fb9" stroke-width=".9"/></svg>Addictions</li>
      <li><svg viewBox="0 0 10 10"><path d="M7 2a3.5 3.5 0 100 6 4 4 0 010-6z" stroke="#1e6fb9" fill="none" stroke-width=".9"/></svg>Sleep Disorders</li>
      <li><svg viewBox="0 0 10 10"><path d="M3 1v8M7 1v8M2 1v3h2V1" stroke="#1e6fb9" fill="none" stroke-width=".9"/></svg>Eating Disorders</li>
      <li><svg viewBox="0 0 10 10"><rect x="1" y="2" width="8" height="6" stroke="#1e6fb9" fill="none" stroke-width=".9"/><circle cx="5" cy="5" r="1.3" stroke="#1e6fb9" fill="none" stroke-width=".7"/></svg>Financial Problems</li>
      <li><svg viewBox="0 0 10 10"><circle cx="3" cy="3" r="1.6" stroke="#1e6fb9" fill="none" stroke-width=".8"/><circle cx="7" cy="4" r="1.3" stroke="#1e6fb9" fill="none" stroke-width=".8"/><path d="M.5 9c0-3 5-3 5 0M5 9c0-2.5 4.5-2.5 4.5 0" stroke="#1e6fb9" fill="none" stroke-width=".8"/></svg>Parenthood</li>
      <li><svg viewBox="0 0 10 10"><path d="M1 3h6l-2-2M9 7H3l2 2" stroke="#1e6fb9" fill="none" stroke-width=".9"/></svg>Relationship</li>
    </ul>
  </aside>

  <div class="hero">
    <div class="hero-photo" role="img" aria-label="Faded photo of a woman sitting in a bright therapy room"></div>
    <nav class="nav" style="left:28px">
      <a>Smart Chatline</a><a>Therapists</a><a>Organizations</a><a>Videos</a><a>Contact</a><a>About</a>
      <a class="donate">Donate</a>
      <span class="lang"><span class="flag"></span>English ▾</span>
    </nav>
  </div>

  <h2 class="welcome-title">Welcome to TovaLamarpe</h2>
  <p class="welcome-text">Lorem ipsum dolor sit amet, consectetur adipiscing elit, sed do eiusmod tempor incididunt ut labore et dolore magna aliqua. Ut enim ad minim veniam, quis nostrud exercitation ullamco laboris nisi ut aliquip ex ea commodo consequat.</p>

  <div class="feature-frame right" style="left:106px;top:393px"></div>
  <div class="feature-media" role="img" aria-label="Photo of two women talking in a counselling session" style="left:103px;top:393px;background:linear-gradient(135deg,#d9d4cc,#8e8a85 60%,#6b7a8c)"></div>
  <h3 class="feature-title" style="left:241px;top:403px">Emergency Mental Help</h3>
  <p class="feature-text" style="left:241px;top:423px;width:180px">Lorem ipsum dolor sit amet, consectetur adipiscing elit, sed do eiusmod tempor incididunt ut labore et dolore magna aliqua. Ut enim ad minim veniam, quis nostrud exercitation ullamco laboris nisi ut aliquip ex ea commodo consequat.</p>
  <span class="btn" style="left:241px;top:471px">More options for Emergency Mental Help</span>

  <h3 class="feature-title" style="left:103px;top:538px">Smart Chatline</h3>
  <p class="feature-text" style="left:103px;top:558px">Lorem ipsum dolor sit amet, consectetur adipiscing elit, sed do eiusmod tempor incididunt ut labore et dolore magna aliqua. Ut enim ad minim veniam, quis nostrud exercitation ullamco laboris nisi ut aliquip ex ea commodo consequat</p>
  <span class="btn" style="left:103px;top:605px"><svg viewBox="0 0 10 10"><path d="M2.2 1.2l1.6 0 .7 2-1 .8c.6 1.3 1.2 1.9 2.5 2.5l.8-1 2 .7v1.6c0 .5-.4.9-.9.9C4.5 8.7 1.3 5.5 1.3 2.1c0-.5.4-.9.9-.9z" fill="#fff"/></svg>052-4400-781</span>
  <div class="feature-frame left" style="left:289px;top:529px"></div>
  <div class="feature-media" role="img" aria-label="Photo of hands holding a paper head with a puzzle heart" style="left:293px;top:529px;background:linear-gradient(135deg,#cdc3b6,#a79a89 55%,#7a6a5c)"></div>

  <div class="feature-frame right" style="left:106px;top:672px"></div>
  <div class="feature-media" role="img" aria-label="Photo of a therapist taking notes beside a patient lying on a couch" style="left:103px;top:672px;background:linear-gradient(135deg,#eeeeec,#cfcdc8 55%,#8f969e)"></div>
  <h3 class="feature-title" style="left:247px;top:676px">Therapists</h3>
  <p class="feature-text" style="left:247px;top:696px">Lorem ipsum dolor sit amet, consectetur adipiscing elit, sed do eiusmod tempor incididunt ut labore et dolore magna aliqua. Ut enim ad minim veniam, quis nostrud exercitation ullamco laboris nisi ut aliquip ex ea commodo consequat.</p>
  <span class="btn" style="left:247px;top:751px">Find Therapists</span>

  <h3 class="feature-title" style="left:103px;top:821px">Organizations</h3>
  <p class="feature-text" style="left:103px;top:843px">Lorem ipsum dolor sit amet, consectetur adipiscing elit, sed do eiusmod tempor incididunt ut labore et dolore magna aliqua. Ut enim ad minim veniam, quis noxercitation ullamco laboris nisi ut aliquip ex ea commodo consequat</p>
  <span class="btn" style="left:103px;top:887px">Find Organizations</span>
  <div class="feature-frame left" style="left:290px;top:810px"></div>
  <div class="feature-media" role="img" aria-label="Photo of two women in conversation on a sofa and yellow armchair" style="left:295px;top:810px;background:linear-gradient(135deg,#d8d6d2,#9a9894 55%,#d1a73a)"></div>

  <div class="feature-frame right" style="left:108px;top:957px"></div>
  <div class="feature-media" role="img" aria-label="Photo of a group therapy session with a distressed man" style="left:105px;top:957px;background:linear-gradient(135deg,#f1f1ef,#cdd0d2 55%,#7f8b97)"></div>
  <h3 class="feature-title" style="left:246px;top:963px">Videos</h3>
  <p class="feature-text" style="left:246px;top:983px">Lorem ipsum dolor sit amet, consectetur adipiscing elit, sed do eiusmod tempor incididunt ut labore et dolore magna aliqua. Ut enim ad minim veniam, quis nostrud exercitation ullamco laboris nisi ut aliquip ex ea commodo consequat.</p>
  <span class="btn" style="left:246px;top:1029px">Video Library</span>

  <footer class="footer">
    <span class="copy"><b>TovaLamarpe</b> - Organization for Mental Health ©2023</span>
    <span class="links">Privacy Policy<span>|</span>Terms</span>
    <span class="stamp">March 01, 2023. Layout_4</span>
  </footer>
</section>

<section class="page page--v2">
  <aside class="sidebar">
    <div class="brand"><span class="brand-dot"></span>TovaLamarpe</div>
    <ul class="cat-list">
      <li><svg viewBox="0 0 10 10"><circle cx="5" cy="5" r="4" fill="#1e6fb9"/></svg>Emergency Mental Help</li>
      <li><svg viewBox="0 0 10 10"><path d="M5 1v4M3 8a2 2 0 004 0 2 2 0 00-4 0" stroke="#1e6fb9" fill="none" stroke-width=".9"/></svg>Suicide</li>
      <li><svg viewBox="0 0 10 10"><circle cx="5" cy="5" r="2.4" stroke="#1e6fb9" fill="none" stroke-width=".9"/><path d="M5 0v2M5 8v2M0 5h2M8 5h2" stroke="#1e6fb9" stroke-width=".9"/></svg>Sexual Assault/<br>Violence Victims</li>
      <li><svg viewBox="0 0 10 10"><circle cx="5" cy="5" r="4" stroke="#1e6fb9" fill="none" stroke-width=".9"/><circle cx="5" cy="5" r="2" stroke="#1e6fb9" fill="none" stroke-width=".7"/></svg>Sexual Assault/<br>Violence Assaulters</li>
      <li><svg viewBox="0 0 10 10"><circle cx="5" cy="3" r="2" stroke="#1e6fb9" fill="none" stroke-width=".9"/><path d="M1 9.5c0-3 8-3 8 0" stroke="#1e6fb9" fill="none" stroke-width=".9"/></svg>Post Trauma</li>
      <li><svg viewBox="0 0 10 10"><circle cx="5" cy="5" r="3.6" stroke="#1e6fb9" fill="none" stroke-width=".9"/><path d="M3.4 6.8c1-1 2.2-1 3.2 0" stroke="#1e6fb9" fill="none" stroke-width=".8"/></svg>Depression</li>
      <li><svg viewBox="0 0 10 10"><path d="M2 9V5a3 3 0 016 0v4" stroke="#1e6fb9" fill="none" stroke-width="1"/></svg>Anxiety</li>
      <li><svg viewBox="0 0 10 10"><circle cx="4.5" cy="4" r="3" stroke="#1e6fb9" fill="none" stroke-width=".9"/><path d="M1 9.5h8" stroke="#1e6fb9" stroke-width=".9"/></svg>Addictions</li>
      <li><svg viewBox="0 0 10 10"><path d="M7 2a3.5 3.5 0 100 6 4 4 0 010-6z" stroke="#1e6fb9" fill="none" stroke-width=".9"/></svg>Sleep Disorders</li>
      <li><svg viewBox="0 0 10 10"><path d="M3 1v8M7 1v8M2 1v3h2V1" stroke="#1e6fb9" fill="none" stroke-width=".9"/></svg>Eating Disorders</li>
      <li><svg viewBox="0 0 10 10"><rect x="1" y="2" width="8" height="6" stroke="#1e6fb9" fill="none" stroke-width=".9"/><circle cx="5" cy="5" r="1.3" stroke="#1e6fb9" fill="none" stroke-width=".7"/></svg>Financial Problems</li>
      <li><svg viewBox="0 0 10 10"><circle cx="3" cy="3" r="1.6" stroke="#1e6fb9" fill="none" stroke-width=".8"/><circle cx="7" cy="4" r="1.3" stroke="#1e6fb9" fill="none" stroke-width=".8"/><path d="M.5 9c0-3 5-3 5 0M5 9c0-2.5 4.5-2.5 4.5 0" stroke="#1e6fb9" fill="none" stroke-width=".8"/></svg>Parenthood</li>
      <li><svg viewBox="0 0 10 10"><path d="M1 3h6l-2-2M9 7H3l2 2" stroke="#1e6fb9" fill="none" stroke-width=".9"/></svg>Relationship</li>
    </ul>
  </aside>

  <div class="hero" role="img" aria-label="Blue to green tinted photo of a counselling session">
    <nav class="nav" style="left:28px">
      <a>Smart Chatline</a><a>Therapists</a><a>Organizations</a><a>Videos</a><a>Contact</a><a>About</a>
      <a class="donate">Donate</a>
      <span class="lang"><span class="flag"></span>English ▾</span>
    </nav>
    <h2 class="hero-title">TovaLamarpe</h2>
    <p class="hero-sub">eiusmod tempor incididunt ut labore et dolore magna aliqua. Ut enim ad minim veniam, quis nostrud exercitation ullamco laboris nisi ut al.</p>
    <span class="scroll-mouse"></span>
  </div>

  <h2 class="welcome-title">Welcome to <b>TovaLamarpe</b></h2>
  <p class="welcome-text">Lorem ipsum dolor sit amet, consectetur adipiscing elit, sed do eiusmod tempor incididunt ut labore et dolore magna aliqua. Ut enim ad minim veniam, quis nostrud exercitation ullamco laboris nisi ut aliquip ex ea commodo consequat.</p>

  <div class="spot-card">
    <div class="media" role="img" aria-label="Photo of two women talking in a counselling session" style="background:linear-gradient(135deg,#d9d4cc,#8e8a85 60%,#6b7a8c)"></div>
    <h3>Emergency Mental Help</h3>
    <p>Lorem ipsum dolor sit amet, consectetur adipiscing elit, sed do eiusmod tempor incididunt ut labore et dolore magna aliqua. Ut enim ad minim veniam, quis nostrud exercitation ullamco laboris nisi ut aliquip ex ea commodo consequat.</p>
    <span class="btn">More options for Emergency Mental Help</span>
  </div>

  <div class="tile" style="left:87px">
    <div class="media" role="img" aria-label="Photo of a hand holding a phone with a chat screen" style="background:linear-gradient(135deg,#8a7566,#3f5a5a 55%,#1c8a7a)"></div>
    <h4>Smart Chatline</h4>
    <p>Lorem ipsum dolor sit amet, consectetur adipiscing elit</p>
    <span class="btn"><svg viewBox="0 0 10 10"><path d="M2.2 1.2l1.6 0 .7 2-1 .8c.6 1.3 1.2 1.9 2.5 2.5l.8-1 2 .7v1.6c0 .5-.4.9-.9.9C4.5 8.7 1.3 5.5 1.3 2.1c0-.5.4-.9.9-.9z" fill="#fff"/></svg>052-4400-781</span>
  </div>
  <div class="tile" style="left:173px">
    <div class="media" role="img" aria-label="Photo of a therapist with a client in an office" style="background:linear-gradient(135deg,#d8d1c6,#b79e80 55%,#8a7a6a)"></div>
    <h4>Therapists</h4>
    <p>Lorem ipsum dolor sit amet, consectetur adipiscing elit</p>
    <span class="btn blue">Find Therapists</span>
  </div>
  <div class="tile" style="left:258px">
    <div class="media" role="img" aria-label="Photo of a small group meeting around a table" style="background:linear-gradient(135deg,#efeeea,#d4cdbf 55%,#8c8478)"></div>
    <h4>Organizations</h4>
    <p>Lorem ipsum dolor sit amet, consectetur adipiscing elit</p>
    <span class="btn blue">Find Organizations</span>
  </div>
  <div class="tile" style="left:344px">
    <div class="media" role="img" aria-label="Photo of a counsellor and client in a bright lounge" style="background:linear-gradient(135deg,#f3f4f5,#cfd5da 55%,#7c8894)"></div>
    <h4>Videos</h4>
    <p>Lorem ipsum dolor sit amet, consectetur adipiscing elit</p>
    <span class="btn">Video Library</span>
  </div>

  <footer class="footer">
    <span class="copy"><b>TovaLamarpe</b> - Organization for Mental Health ©2023</span>
    <span class="links">Privacy Policy<span>|</span>Terms</span>
    <span class="stamp">March 01, 2023. Layout_4</span>
  </footer>
</section>

<div class="thanks">
  <div class="line1">Thank You For</div>
  <div class="line2">Watching</div>
</div>

</body>
</html>
```